Etiketten-Design für Kaffeetüten
Zielgruppe
Wir stellen eine nachhaltige alternative zu herkömmlichem Bohnenkaffee her.
Regional, nachhaltig und koffeinfrei.
Hierzu verwenden wir Süßlupinen die wir von einem Partnerbauern aus Niedersachsen beziehen. Diese Lupinen werden wie herkömmlicher Kaffee in einem Trommelröster geröstet und anschließend gemahlen.
Unser Lupinenkaffee kann wie herkömmlicher Kaffee im Filter in der Frenchpress oder in einem Espressokocher zubereitet werden.
Wir bieten unseren Kunden zwei verschiedene Sorten an, eine 'Mild' und eine 'Klassisch'.
Die Zielgruppe sind ernährungsbewusste Menschen die gezielt eine alternative zu herkömmlichen Bohnenkaffee suchen. (Koffeinfreier Kaffee, Getreidekaffee)
Aufgabenstellung
Wir möchten ein modernes Design des Etiketts, das den Stil des Logos widerspiegelt. Die beiden Sorten 'Mild' und 'Klassisch' sollten gut von einander zu unterscheiden sein.
Es gibt ein Etikett für die Vorderseite, hier soll die Produktbezeichnung 'Lupinenkaffee' sowie die Mengenangabe '500g' stehen.
Ggf. 3 Icons für mögliche Brühmethoden (Filter, Frenchpress, Espressokocher)
Auf dem Etikett der Rückseite müssen zum einen die Zutaten, die Zubereitung sowie die Nährwertangaben (in TabellenForm) angegeben werden. Sowie ein EAN Code die Herstellerangaben und die Adresse der Homepage.
FENNO BREW – Deine nachhaltige Kaffeealternative
Zutaten: weiße Süßlupinen, geröstet
Zubereitung: Du kannst Deinen Lupinenkaffee mit der French Press, dem klassischen Filter oder dem Espressokocher zubereiten. Für den optimalen Geschmack empfehlen wir 8g Kaffeepulver für 100ml.
Hersteller:
FENNO GmbH
Birkenhainer Weg 57
40213 Düsseldorf
www.FENNOBREW.de
 Nährwertangaben für 100 ml Kaffee
Energie 12kj - 5 kcal
Fett <0,1g
Davon gesättigt <0,1g
Kohlenhydrate <1,0g
Davon Zucker <0,05g
Eiweiß <1,0g
Salz <0,05g
Die Kaffeetüte, auf die das Etikett geklebt wird, ist in einer braunen Kartonfarbe.
Das Etikett für die Kaffeetüten hat die Maße 7x11.
Das Logo hat die Schriftart 'Cera'. Die verwendete Schriftart sollte möglichst gleich sein, oder gut damit harmonieren.

```html
<!DOCTYPE html>
<html lang="de">
<head>
<meta charset="utf-8">
<title>Lupinen Kaffee – Etikett Klassisch</title>
<link rel="stylesheet" href="https://fonts.googleapis.com/css2?family=Jost:wght@300;400&display=swap">
<style>
  :root {
    --ink: #111111;
    --label-black: #1b1b1b;
    --gold: #c0912a;
    --teal: #4f98a8;
    --white: #ffffff;
    --page: #e9e4dc;
  }
  html, body {
    margin: 0;
    padding: 0;
    width: 762px;
    height: 1200px;
    overflow: hidden;
    background: var(--page);
  }
  .label {
    position: relative;
    width: 762px;
    height: 1200px;
    overflow: hidden;
    background: var(--label-black);
    font-family: "Jost", "Helvetica Neue", Arial, sans-serif;
  }
  .stripes {
    position: absolute;
    left: 0;
    width: 762px;
    background: repeating-linear-gradient(90deg,
      var(--gold) 0 14px,
      var(--label-black) 14px 30px,
      var(--teal) 30px 44px,
      var(--label-black) 44px 58px,
      var(--white) 58px 68px,
      var(--label-black) 68px 84px);
  }
  .stripes--top { top: 397px; height: 197px; }
  .stripes--bottom { top: 996px; height: 204px; }

  .variety-corner {
    position: absolute;
    top: 0;
    left: 0;
    width: 277px;
    height: 190px;
    background: var(--teal);
    clip-path: polygon(0 0, 100% 0, 0 100%);
  }
  .variety-name {
    position: absolute;
    left: 24px;
    top: 118px;
    margin: 0;
    color: var(--white);
    font-size: 33px;
    line-height: 1;
    font-weight: 400;
    transform: rotate(-35deg);
    transform-origin: left top;
  }

  .brand-seal {
    position: absolute;
    left: 172px;
    top: 127px;
    width: 436px;
    height: 436px;
    border-radius: 50%;
    background: var(--label-black);
  }
  .brand-ring {
    position: absolute;
    left: 18px;
    top: 18px;
    width: 400px;
    height: 400px;
  }
  .brand-name {
    position: absolute;
    left: 0;
    top: 0;
    width: 436px;
    height: 436px;
    display: flex;
    align-items: center;
    justify-content: center;
    color: var(--gold);
    font-size: 42px;
    font-weight: 400;
    letter-spacing: 3px;
  }

  .title-band {
    position: absolute;
    left: 0;
    top: 594px;
    width: 762px;
    height: 402px;
    background: var(--gold);
  }
  .title-word {
    position: absolute;
    left: 0;
    width: 762px;
    margin: 0;
    text-align: center;
    color: var(--ink);
    font-weight: 300;
    font-size: 140px;
    line-height: 1;
    box-sizing: border-box;
  }
  .title-word--top { top: 28px; letter-spacing: 26px; padding-left: 26px; }
  .title-word--bottom { top: 232px; letter-spacing: 48px; padding-left: 48px; }
  .title-rule {
    position: absolute;
    left: 46px;
    top: 188px;
    width: 670px;
    height: 4px;
    background: var(--ink);
  }

  .weight-corner {
    position: absolute;
    right: 0;
    bottom: 0;
    width: 245px;
    height: 167px;
    background: var(--white);
    clip-path: polygon(100% 0, 100% 100%, 0 100%);
  }
  .net-weight {
    position: absolute;
    right: 22px;
    bottom: 16px;
    margin: 0;
    color: var(--ink);
    font-size: 40px;
    line-height: 1;
    font-weight: 400;
  }
</style>
</head>
<body>
  <main class="label">
    <div class="variety-corner"></div>
    <p class="variety-name">Klassisch</p>

    <div class="stripes stripes--top"></div>
    <div class="stripes stripes--bottom"></div>

    <div class="brand-seal">
      <svg class="brand-ring" viewBox="0 0 400 400" aria-hidden="true">
        <circle cx="200" cy="200" r="196" fill="none" stroke="#c0912a" stroke-width="7"/>
      </svg>
      <span class="brand-name">HALMWERK</span>
    </div>

    <section class="title-band">
      <h1 class="title-word title-word--top">LUPINEN</h1>
      <div class="title-rule"></div>
      <h2 class="title-word title-word--bottom">KAFFEE</h2>
    </section>

    <div class="weight-corner"></div>
    <p class="net-weight">500g</p>
  </main>
</body>
</html>
```